Velorak app icon design

We are building an Velorak app and would like some good looking icons to replace the boring ones we have created ourselves.

Please see attached screen shots.

The icons toggle "Active/Inactive" where the inactive is shaded out.

Building

```html
<!DOCTYPE html>
<html lang="en">
<head>
<meta charset="utf-8">
<title>Velorak search icon states</title>
<link rel="stylesheet" href="https://fonts.googleapis.com/css2?family=Exo+2:wght@600;700&family=Roboto:wght@700&family=Share+Tech+Mono&family=Space+Mono:wght@700&display=swap">
<style>
  :root {
    --canvas: #ffffff;
    --label-bar: #000000;
    --header-blue: #0b5a9c;
    --header-line: #29abe2;
    --home-btn: #2a7cc7;
    --cyan: #29abe2;
    --navy: #0d5696;
    --navy-strip: #0a4f8c;
    --tile-grey: #d2d3d5;
    --divider: #ffffff;
    --list-bg: #f2f2f3;
    --card-border: #c8c8c8;
    --search-top: #dfe4ea;
    --search-bottom: #7d9bbd;
    --footer-band: #000000;
  }
  * { box-sizing: border-box; margin: 0; padding: 0; }
  html, body { width: 1200px; height: 669px; overflow: hidden; background: var(--canvas); }
  .board { position: relative; width: 1200px; height: 669px; }

  .screen {
    position: absolute; top: 25px; width: 357px; height: 476px;
    background: var(--list-bg);
    --icon: var(--cyan); --strip: var(--cyan); --text: var(--cyan); --item-icon: var(--cyan);
  }
  .screen--normal { left: 27px; }
  .screen--active { left: 410px; top: 27px; --icon: var(--navy); --strip: var(--navy-strip); --text: var(--navy); --item-icon: var(--navy); }
  .screen--single { left: 803px; top: 27px; --text: var(--navy); }

  .state-label {
    height: 18px; background: var(--label-bar); color: #fff;
    font: 700 15px/18px "Space Mono", monospace; text-align: center;
  }
  .screen--single .state-label { text-align: right; padding-right: 28px; }

  .app-header {
    position: relative; height: 54px; background: var(--header-blue);
    border-top: 2px solid var(--header-line); border-bottom: 2px solid var(--header-line);
  }
  .home-button {
    position: absolute; left: 10px; top: 10px; width: 80px; height: 28px;
    background: var(--home-btn); color: #fff;
    clip-path: polygon(10px 0, 100% 0, 100% 100%, 10px 100%, 0 50%);
    font: 600 15px/28px "Exo 2", sans-serif; text-align: center; padding-left: 6px;
  }
  .screen-title {
    position: absolute; left: 127px; top: 9px; color: #fff;
    font: 700 27px/1 "Exo 2", sans-serif; letter-spacing: 2px;
  }

  .category-tabs { display: flex; height: 82px; border-bottom: 2px solid var(--header-line); background: var(--divider); gap: 1px; }
  .tab { flex: 1; display: flex; flex-direction: column; background: var(--tile-grey); color: var(--icon); }
  .tab svg { flex: 1; width: 100%; }
  .tab-name {
    height: 12px; background: var(--strip); color: #fff;
    font: 700 8.5px/12px "Roboto", sans-serif; text-align: center; letter-spacing: 0.5px;
  }
  .tab--selected { color: var(--navy); }
  .tab--selected .tab-name { background: var(--label-bar); }
  .tab--current .tab-name { background: var(--navy-strip); }

  .search-band {
    height: 52px; padding: 12px 12px 0;
    background: linear-gradient(var(--search-top), var(--search-bottom));
  }
  .search-field { height: 27px; background: #fff; border: 1px solid var(--home-btn); border-radius: 13px; }

  .result-list { list-style: none; padding: 6px 10px 0 6px; }
  .result {
    display: flex; height: 58px; margin-bottom: 6px; background: #fff;
    border: 1px solid var(--card-border); border-left: none; border-radius: 0 9px 9px 0;
  }
  .result-icon { width: 60px; background: var(--tile-grey); border-top: 2px solid var(--cyan); color: var(--item-icon); display: flex; align-items: center; justify-content: center; }
  .result-icon svg { width: 42px; height: 42px; }
  .result-address { padding: 9px 0 0 12px; color: var(--text); font: 18px/19px "Share Tech Mono", monospace; }
  .result--person .result-address { padding-left: 15px; }

  .footer-band { position: absolute; left: 14px; top: 542px; width: 1172px; height: 115px; background: var(--footer-band); }
</style>
</head>
<body>
<svg width="0" height="0" style="position:absolute" aria-hidden="true">
  <defs>
    <symbol id="icon-folder" viewBox="0 0 70 70"><path d="M16 20h14l4 5h20v26H16z" fill="currentColor"/></symbol>
    <symbol id="icon-folder-open" viewBox="0 0 70 70"><path d="M15 22h12l4 4h22v6H15z" fill="currentColor"/><path d="M14 34h43l-4 20H18z" fill="currentColor"/><path d="M18 28h33v4H18z" fill="#fff"/></symbol>
    <symbol id="icon-house" viewBox="0 0 70 70"><path d="M35 13 12 35l4 4 19-18 19 18 4-4z" fill="currentColor"/><path d="M20 38 35 24l15 14v17H39V44h-8v11H20z" fill="currentColor"/><rect x="44" y="16" width="5" height="10" fill="currentColor"/></symbol>
    <symbol id="icon-person" viewBox="0 0 70 70"><circle cx="35" cy="28" r="11" fill="currentColor"/><path d="M16 56c0-10 8-15 19-15s19 5 19 15z" fill="currentColor"/></symbol>
    <symbol id="icon-staff" viewBox="0 0 70 70"><circle cx="28" cy="27" r="10" fill="currentColor"/><path d="M10 54c0-9 7-14 18-14s18 5 18 14z" fill="currentColor"/><circle cx="49" cy="33" r="8" fill="currentColor"/><path d="M36 56c0-8 6-12 13-12s13 4 13 12z" fill="currentColor"/></symbol>
  </defs>
</svg>

<main class="board">
  <section class="screen screen--normal">
    <div class="state-label">normal</div>
    <header class="app-header"><span class="home-button">Home</span><h1 class="screen-title">Search</h1></header>
    <nav class="category-tabs">
      <div class="tab"><svg viewBox="0 0 70 70"><use href="#icon-folder"/></svg><span class="tab-name">PORTFOLIO</span></div>
      <div class="tab"><svg viewBox="0 0 70 70"><use href="#icon-house"/></svg><span class="tab-name">PROPERTY</span></div>
      <div class="tab"><svg viewBox="0 0 70 70"><use href="#icon-person"/></svg><span class="tab-name">OWNER</span></div>
      <div class="tab"><svg viewBox="0 0 70 70"><use href="#icon-person"/></svg><span class="tab-name">TENANT</span></div>
      <div class="tab"><svg viewBox="0 0 70 70"><use href="#icon-staff"/></svg><span class="tab-name">STAFF</span></div>
    </nav>
    <div class="search-band"><div class="search-field"></div></div>
    <ul class="result-list">
      <li class="result"><span class="result-icon"><svg viewBox="0 0 70 70"><use href="#icon-house"/></svg></span><p class="result-address">10/15 Harlow Street<br>ARDENVALE EAST NSW 2041</p></li>
      <li class="result"><span class="result-icon"><svg viewBox="0 0 70 70"><use href="#icon-house"/></svg></span><p class="result-address">10/15 Harlow Street<br>ARDENVALE EAST NSW 2041</p></li>
      <li class="result result--person"><span class="result-icon"><svg viewBox="0 0 70 70"><use href="#icon-person"/></svg></span><p class="result-address">10/15 Harlow Street<br>ARDENVALE EAST NSW 2041</p></li>
      <li class="result result--person"><span class="result-icon"><svg viewBox="0 0 70 70"><use href="#icon-person"/></svg></span><p class="result-address">10/15 Harlow Street<br>ARDENVALE EAST NSW 2041</p></li>
    </ul>
  </section>

  <section class="screen screen--active">
    <div class="state-label">when active</div>
    <header class="app-header"><span class="home-button">Home</span><h1 class="screen-title">Search</h1></header>
    <nav class="category-tabs">
      <div class="tab"><svg viewBox="0 0 70 70"><use href="#icon-folder"/></svg><span class="tab-name">PORTFOLIO</span></div>
      <div class="tab"><svg viewBox="0 0 70 70"><use href="#icon-house"/></svg><span class="tab-name">PROPERTY</span></div>
      <div class="tab"><svg viewBox="0 0 70 70"><use href="#icon-person"/></svg><span class="tab-name">OWNER</span></div>
      <div class="tab"><svg viewBox="0 0 70 70"><use href="#icon-person"/></svg><span class="tab-name">TENANT</span></div>
      <div class="tab"><svg viewBox="0 0 70 70"><use href="#icon-staff"/></svg><span class="tab-name">STAFF</span></div>
    </nav>
    <div class="search-band"><div class="search-field"></div></div>
    <ul class="result-list">
      <li class="result"><span class="result-icon"><svg viewBox="0 0 70 70"><use href="#icon-house"/></svg></span><p class="result-address">10/15 Harlow Street<br>ARDENVALE EAST NSW 2041</p></li>
      <li class="result"><span class="result-icon"><svg viewBox="0 0 70 70"><use href="#icon-house"/></svg></span><p class="result-address">10/15 Harlow Street<br>ARDENVALE EAST NSW 2041</p></li>
      <li class="result result--person"><span class="result-icon"><svg viewBox="0 0 70 70"><use href="#icon-person"/></svg></span><p class="result-address">10/15 Harlow Street<br>ARDENVALE EAST NSW 2041</p></li>
      <li class="result result--person"><span class="result-icon"><svg viewBox="0 0 70 70"><use href="#icon-person"/></svg></span><p class="result-address">10/15 Harlow Street<br>ARDENVALE EAST NSW 2041</p></li>
    </ul>
  </section>

  <section class="screen screen--single">
    <div class="state-label">when active only one</div>
    <header class="app-header"><span class="home-button">Home</span><h1 class="screen-title">Search</h1></header>
    <nav class="category-tabs">
      <div class="tab tab--selected tab--current"><svg viewBox="0 0 70 70"><use href="#icon-folder-open"/></svg><span class="tab-name">ALL</span></div>
      <div class="tab"><svg viewBox="0 0 70 70"><use href="#icon-house"/></svg><span class="tab-name">PROPERTY</span></div>
      <div class="tab"><svg viewBox="0 0 70 70"><use href="#icon-person"/></svg><span class="tab-name">OWNER</span></div>
      <div class="tab"><svg viewBox="0 0 70 70"><use href="#icon-person"/></svg><span class="tab-name">TENANT</span></div>
      <div class="tab"><svg viewBox="0 0 70 70"><use href="#icon-staff"/></svg><span class="tab-name">STAFF</span></div>
    </nav>
    <div class="search-band"><div class="search-field"></div></div>
    <ul class="result-list">
      <li class="result"><span class="result-icon"><svg viewBox="0 0 70 70"><use href="#icon-house"/></svg></span><p class="result-address">10/15 Harlow Street<br>ARDENVALE EAST NSW 2041</p></li>
      <li class="result"><span class="result-icon"><svg viewBox="0 0 70 70"><use href="#icon-house"/></svg></span><p class="result-address">10/15 Harlow Street<br>ARDENVALE EAST NSW 2041</p></li>
      <li class="result result--person"><span class="result-icon"><svg viewBox="0 0 70 70"><use href="#icon-person"/></svg></span><p class="result-address">10/15 Harlow Street<br>ARDENVALE EAST NSW 2041</p></li>
      <li class="result result--person"><span class="result-icon"><svg viewBox="0 0 70 70"><use href="#icon-person"/></svg></span><p class="result-address">10/15 Harlow Street<br>ARDENVALE EAST NSW 2041</p></li>
    </ul>
  </section>

  <footer class="footer-band"></footer>
</main>
</body>
</html>
```